"Landing Page Design for Premium Eco-Friendly Laundry Strips – Plooifris.nl"

We need a visually appealing and high-converting landing page for our premium laundry strips, emphasizing luxury, sustainability, and ease of use. The page should include sections such as:

Hero Section: A compelling introduction with a strong headline, subheadline, and a clear call-to-action (CTA).
Product Benefits: Highlighting key features like eco-friendliness, long-lasting scent, and hypoallergenic qualities.
Product Description: Focusing on innovation and sustainability.
How It Works: Simple, visual steps for using the product.
Customer Reviews: Authentic testimonials to build trust and social proof.
FAQ Section: Addressing common concerns about the product.
The design should maintain a luxurious aesthetic while ensuring clarity and user-friendliness. We also offer free shipping on all orders, a key differentiator to be prominently displayed. All texts and translations are already provided for implementation. Please deliver the design in Figma format."

Target Market(s)

"Eco-conscious consumers and families seeking premium and sustainable laundry solutions. Target age group: 25-50, predominantly women who prioritize luxury and environmental impact."

Industry/Entity Type

"Laundry care and eco-friendly consumer goods."

Coding

Requirements
Must have
• A visually luxurious design emphasizing premium quality and eco-friendliness. Clear call-to-actions (e.g., 'Try Now – Free Shipping'). Sections for product benefits, how it works, customer reviews, and FAQ. Highlight free shipping with no minimum order prominently."
Nice to have
• Elegant, minimalist animations to enhance the premium feel. Subtle use of gold and black to emphasize luxury, with a touch of green for sustainability. Interactive customer reviews section (e.g., carousel or testimonials)."
Should not have
• Overly cluttered designs or overwhelming text blocks. Generic stock photos not aligned with our brand identity. Bright or overly playful color schemes that detract from the premium feel."

```html
<!DOCTYPE html>
<html lang="en">
<head>
<meta charset="utf-8">
<title>Plooifris.nl – Premium Laundry Strips</title>
<link href="https://fonts.googleapis.com/css2?family=Poppins:wght@400;500;600;700&display=swap" rel="stylesheet">
<style>
:root{
  --gold:#c9a13b;
  --gold-light:#e6c76a;
  --gold-dark:#a47c1f;
  --black:#111111;
  --dark-panel:#1f2024;
  --cream:#fcf3e2;
  --cream-soft:#fdf8ee;
  --text:#1a1a1a;
  --muted:#6b6b6b;
  --white:#ffffff;
  --line:#e6e0d4;
}
*{box-sizing:border-box;margin:0;padding:0}
html,body{width:1200px;height:4156px;overflow:hidden}
body{font-family:'Poppins',sans-serif;color:var(--text);background:var(--white);position:relative}

/* header */
.site-header{position:absolute;top:0;left:0;width:1200px;height:80px;z-index:5}
.brand{position:absolute;display:flex;align-items:center;gap:10px;font-weight:600;color:var(--gold);font-size:20px}
.brand-mark{width:26px;height:26px;background:var(--gold)}
.site-header .brand{left:140px;top:26px}
.btn-gold{display:inline-block;background:linear-gradient(90deg,var(--gold-dark),var(--gold-light));color:var(--black);font-weight:600;border-radius:8px;text-align:center}
.contact-btn{position:absolute;left:884px;top:34px;width:120px;height:34px;line-height:34px;font-size:13px}
.menu-dot{position:absolute;left:1016px;top:34px;width:34px;height:34px;border-radius:50%;border:3px solid var(--black);background:var(--white)}

/* hero */
.hero{position:absolute;top:0;left:0;width:1200px;height:740px;background:linear-gradient(90deg,#fbf5ea 0%,#f5ece0 55%,#efe5d8 100%);overflow:hidden}
.hero-photo{position:absolute;left:620px;top:0;width:580px;height:740px;background:linear-gradient(180deg,#ece3d7,#d9cfc4 60%,#f1ebe3)}
.hero-title{position:absolute;left:140px;top:330px;width:560px;font-size:46px;line-height:58px;font-weight:700;color:var(--black);z-index:2}
.hero-text{position:absolute;left:140px;top:520px;width:480px;font-size:15px;line-height:24px;color:#333;z-index:2}
.hero-cta{position:absolute;left:140px;top:584px;width:180px;height:40px;line-height:40px;font-size:13px;z-index:2}
.hero-wave{position:absolute;left:0;top:660px;width:1200px;height:90px}

/* section titles */
.section-title{position:absolute;left:0;width:1200px;text-align:center;font-size:32px;font-weight:700;color:var(--black)}
.title-rule{position:absolute;left:570px;width:60px;height:4px;background:var(--gold);border-radius:2px}

/* features */
.feature{position:absolute;width:300px}
.feature h3{font-size:15px;font-weight:600;margin-bottom:4px}
.feature p{font-size:11px;line-height:16px;color:var(--muted)}
.feature.left{text-align:right}
.icon-badge{position:absolute;width:84px;height:84px;border-radius:50%;background:radial-gradient(circle at 35% 30%,var(--gold-light),var(--gold-dark));box-shadow:0 4px 10px rgba(0,0,0,.15);display:flex;align-items:center;justify-content:center}
.icon-badge svg{width:38px;height:38px}
.center-seal{position:absolute;left:505px;top:985px;width:190px;height:190px;border-radius:50%;background:var(--black);border:6px solid var(--gold);display:flex;align-items:center;justify-content:center;color:var(--gold);font-weight:600;font-size:24px}
.orbit{position:absolute;left:480px;top:960px;width:240px;height:240px;border-radius:50%;border:2px dashed var(--line)}

/* product */
.product{position:absolute;top:1380px;left:0;width:1200px;height:640px}
.product-bg{position:absolute;inset:0}
.product-box{position:absolute;left:200px;top:100px;width:320px;height:480px;background:linear-gradient(135deg,#1b1b1b 0%,#2d2a22 60%,#b8923a 100%);border-radius:6px;box-shadow:14px 18px 30px rgba(0,0,0,.25)}
.product-title{position:absolute;left:650px;top:300px;width:400px;font-size:34px;line-height:44px;font-weight:700}
.product-text{position:absolute;left:650px;top:410px;width:400px;font-size:14px;line-height:23px;color:#333}

/* steps */
.steps-line{position:absolute;left:0;top:2210px;width:1200px;height:140px}
.step{position:absolute;top:2250px;width:220px;text-align:center}
.step .icon-badge{position:relative;margin:0 auto 20px;width:72px;height:72px}
.step .icon-badge svg{width:32px;height:32px}
.step p{font-size:13px;line-height:20px;font-weight:500}

/* reviews */
.reviews{position:absolute;top:2508px;left:0;width:1200px;height:540px}
.review-photo{position:absolute;left:0;top:0;width:600px;height:540px;background:linear-gradient(160deg,#ece6df,#cfc3b6 55%,#e9e3dc)}
.play-btn{position:absolute;left:264px;top:224px;width:72px;height:72px;border-radius:50%;background:#e02424;display:flex;align-items:center;justify-content:center}
.review-panel{position:absolute;left:600px;top:0;width:600px;height:540px;background:var(--dark-panel)}
.review-panel h2{position:absolute;left:48px;top:70px;color:var(--white);font-size:30px;font-weight:700}
.nav-arrow{position:absolute;left:546px;width:30px;height:30px;border-radius:50%;background:var(--gold);display:flex;align-items:center;justify-content:center}
.review-card{position:absolute;left:60px;top:220px;width:440px;height:220px;background:var(--white);border-radius:6px;text-align:center;padding:70px 50px 0}
.quote-circle{position:absolute;left:190px;top:-30px;width:60px;height:60px;border-radius:50%;background:var(--white);border:3px solid var(--gold);display:flex;align-items:center;justify-content:center;color:var(--gold);font-size:34px;font-weight:700;line-height:1}
.review-card .quote{font-size:13px;line-height:20px;color:#444}
.review-card .name{font-size:15px;font-weight:600;margin-top:14px}
.review-card .role{font-size:12px;color:var(--muted)}

/* faq */
.faq-item{position:absolute;left:280px;width:660px;border:1px solid var(--line);border-radius:6px;background:var(--white);box-shadow:0 2px 8px rgba(0,0,0,.05)}
.faq-q{display:flex;justify-content:space-between;align-items:center;padding:0 22px;height:48px;font-size:14px;font-weight:500}
.faq-a{padding:14px 22px 18px;font-size:13px;line-height:20px;color:var(--muted);border-top:1px solid var(--line)}
.faq-cta{position:absolute;left:480px;top:3572px;width:240px;height:40px;line-height:40px;font-size:13px}

/* cta banner */
.cta-banner{position:absolute;left:140px;top:3690px;width:920px;height:210px;border-radius:18px;background:linear-gradient(90deg,var(--gold-dark),var(--gold-light) 50%,var(--gold-dark));text-align:center;z-index:3}
.cta-banner h2{margin-top:52px;font-size:20px;line-height:30px;font-weight:700;color:var(--black)}
.cta-banner .order-btn{display:inline-block;margin-top:16px;width:120px;height:38px;line-height:38px;background:var(--white);border-radius:19px;font-size:13px;font-weight:600}

/* footer */
.site-footer{position:absolute;left:0;top:3830px;width:1200px;height:326px;background:var(--black);color:var(--white)}
.site-footer .brand{left:210px;top:160px;font-size:24px}
.footer-col{position:absolute;top:160px;display:flex;gap:12px;font-size:13px;line-height:20px}
.footer-col svg{flex:none;width:20px;height:20px;margin-top:2px}
.footer-rule{position:absolute;left:140px;top:272px;width:920px;height:1px;background:#333}
.copyright{position:absolute;left:140px;top:290px;font-size:12px;color:#ccc}
.socials{position:absolute;left:990px;top:286px;display:flex;gap:8px}
.socials span{width:22px;height:22px;border-radius:50%;background:var(--gold)}
</style>
</head>
<body>

<section class="hero">
  <div class="hero-photo" role="img" aria-label="Photo of a smiling woman holding a laundry basket of fresh clothes in a bright bedroom"></div>
  <h1 class="hero-title">Experience Luxury<br>And Sustainability in<br>Every Wash</h1>
  <p class="hero-text">Discover Plooifris's premium laundry strips – where sophistication meets ecological consciousness.</p>
  <a class="btn-gold hero-cta">Always Free Shipping!</a>
  <svg class="hero-wave" viewBox="0 0 1200 90" preserveAspectRatio="none"><path d="M0 40 C300 90 600 0 900 40 C1050 60 1150 30 1200 20 L1200 90 L0 90Z" fill="#ffffff"/></svg>
</section>

<header class="site-header">
  <div class="brand"><span class="brand-mark"></span>Plooifris</div>
  <a class="btn-gold contact-btn">Contact Us</a>
  <span class="menu-dot"></span>
</header>

<h2 class="section-title" style="top:815px">Why Choose Plooifris Laundry Strips?</h2>
<div class="title-rule" style="top:872px"></div>

<div class="orbit"></div>
<div class="center-seal">Plooifris</div>

<div class="icon-badge" style="left:530px;top:918px"><svg viewBox="0 0 40 40" fill="none" stroke="#fff" stroke-width="2.5"><path d="M10 30 C10 14 22 8 32 8 C32 22 24 30 12 30Z"/><path d="M10 30 L22 18"/></svg></div>
<div class="feature left" style="left:210px;top:934px"><h3>Eco-Friendly</h3><p>100% biodegradable and plastic-free, kind to nature and water.</p></div>

<div class="icon-badge" style="left:710px;top:918px"><svg viewBox="0 0 40 40" fill="none" stroke="#fff" stroke-width="2.5"><circle cx="20" cy="20" r="13"/><path d="M20 12 V20 L26 24"/></svg></div>
<div class="feature" style="left:810px;top:934px"><h3>Long-Lasting Scent</h3><p>A delightful fresh scent that lingers for days.</p></div>

<div class="icon-badge" style="left:455px;top:1040px"><svg viewBox="0 0 40 40" fill="none" stroke="#fff" stroke-width="2.5"><path d="M14 8 L8 12 L11 18 L13 17 V32 H27 V17 L29 18 L32 12 L26 8 C24 11 16 11 14 8Z"/></svg></div>
<div class="feature left" style="left:135px;top:1056px"><h3>Suitable for All Fabrics</h3><p>Safe for delicate garments, whites, colours and darks.</p></div>

<div class="icon-badge" style="left:785px;top:1040px"><svg viewBox="0 0 40 40" fill="none" stroke="#fff" stroke-width="2.5"><path d="M20 7 L31 11 V20 C31 27 26 31 20 33 C14 31 9 27 9 20 V11Z"/><path d="M15 20 L19 24 L26 16"/></svg></div>
<div class="feature" style="left:885px;top:1056px"><h3>Hypoallergenic</h3><p>Gentle for sensitive skin and baby clothing.</p></div>

<div class="icon-badge" style="left:530px;top:1162px"><svg viewBox="0 0 40 40" fill="none" stroke="#fff" stroke-width="2.5"><path d="M8 14 L20 8 L32 14 V27 L20 33 L8 27Z"/><path d="M8 14 L20 20 L32 14 M20 20 V33"/></svg></div>
<div class="feature left" style="left:210px;top:1178px"><h3>Compact and User-Friendly</h3><p>No mess with heavy bottles – just tear, add and wash.</p></div>

<div class="icon-badge" style="left:710px;top:1162px"><svg viewBox="0 0 40 40" fill="none" stroke="#fff" stroke-width="2.5"><path d="M5 12 H24 V27 H5Z M24 17 H31 L35 22 V27 H24"/><circle cx="11" cy="29" r="3"/><circle cx="29" cy="29" r="3"/></svg></div>
<div class="feature" style="left:810px;top:1178px"><h3>Always Free Shipping</h3><p>No minimum order quantity required.</p></div>

<section class="product">
  <svg class="product-bg" viewBox="0 0 1200 640" preserveAspectRatio="none"><path d="M0 40 C250 0 450 70 700 30 C900 0 1050 40 1200 20 V620 C900 660 600 600 300 630 C150 645 60 620 0 630Z" fill="#fcf3e2"/></svg>
  <div class="product-box" role="img" aria-label="Product box of Plooifris laundry strips in black and gold packaging"></div>
  <h2 class="product-title">The Future of Laundry<br>Is Here</h2>
  <p class="product-text">Our Plooifris Laundry Strips combine innovation with sustainability. With just one strip per load, enjoy clean and beautifully scented laundry without burdening the environment. No plastic bottles, no waste – just pure washing power in a convenient strip.</p>
</section>

<h2 class="section-title" style="top:2125px">How to Use Laundry Strips</h2>
<div class="title-rule" style="top:2180px"></div>
<svg class="steps-line" viewBox="0 0 1200 140" preserveAspectRatio="none"><path d="M60 80 C180 20 240 110 360 70 C480 30 520 110 620 70 C740 25 780 110 880 70 C980 30 1060 100 1160 60" fill="none" stroke="#d8d2c5" stroke-width="2"/></svg>

<div class="step" style="left:125px"><div class="icon-badge"><svg viewBox="0 0 40 40" fill="none" stroke="#fff" stroke-width="2.5"><rect x="10" y="8" width="20" height="24" rx="2"/><path d="M10 16 H30"/></svg></div><p>Tear off a laundry strip.</p></div>
<div class="step" style="left:365px"><div class="icon-badge"><svg viewBox="0 0 40 40" fill="none" stroke="#fff" stroke-width="2.5"><rect x="9" y="7" width="22" height="27" rx="2"/><circle cx="20" cy="22" r="7"/></svg></div><p>Place the strip directly in the drum with your laundry.</p></div>
<div class="step" style="left:605px"><div class="icon-badge"><svg viewBox="0 0 40 40" fill="none" stroke="#fff" stroke-width="2.5"><circle cx="20" cy="20" r="12"/><path d="M17 14 L26 20 L17 26Z"/></svg></div><p>Start the washing machine and let the strip do its work.</p></div>
<div class="step" style="left:845px"><div class="icon-badge"><svg viewBox="0 0 40 40" fill="none" stroke="#fff" stroke-width="2.5"><path d="M14 8 L8 12 L11 18 L13 17 V32 H27 V17 L29 18 L32 12 L26 8 C24 11 16 11 14 8Z"/></svg></div><p>Enjoy perfectly clean and fresh-smelling clothes!</p></div>

<section class="reviews">
  <div class="review-photo" role="img" aria-label="Photo of a woman loading laundry into a washing machine"></div>
  <div class="play-btn"><svg width="28" height="28" viewBox="0 0 28 28"><path d="M9 6 L22 14 L9 22Z" fill="#fff"/></svg></div>
  <div class="review-panel">
    <h2>What Our Customers Say</h2>
    <div class="nav-arrow" style="top:70px"><svg width="14" height="14" viewBox="0 0 14 14"><path d="M9 2 L4 7 L9 12" fill="none" stroke="#111" stroke-width="2"/></svg></div>
    <div class="nav-arrow" style="top:108px"><svg width="14" height="14" viewBox="0 0 14 14"><path d="M5 2 L10 7 L5 12" fill="none" stroke="#111" stroke-width="2"/></svg></div>
    <div class="review-card">
      <div class="quote-circle">“</div>
      <p class="quote">Since using Plooifris, my laundry feels fresher and more luxurious than ever.</p>
      <p class="name">Lotte</p>
      <p class="role">Lorem ipsum is simply dummy text of the</p>
    </div>
  </div>
</section>

<h2 class="section-title" style="top:3112px">Do You Have Any Questions?</h2>

<div class="faq-item" style="top:3226px">
  <div class="faq-q">Are the strips suitable for people with sensitive skin?<svg width="14" height="14" viewBox="0 0 14 14"><path d="M2 5 L7 10 L12 5" fill="none" stroke="#111" stroke-width="2"/></svg></div>
  <div class="faq-a">Yes, our strips are hypoallergenic and dermatologically tested, making them safe for sensitive skin.</div>
</div>
<div class="faq-item" style="top:3380px">
  <div class="faq-q">How many washes does one pack contain?<svg width="14" height="14" viewBox="0 0 14 14"><path d="M7 1 V13 M1 7 H13" stroke="#111" stroke-width="2"/></svg></div>
</div>
<div class="faq-item" style="top:3448px">
  <div class="faq-q">Do the strips work at low temperatures?<svg width="14" height="14" viewBox="0 0 14 14"><path d="M7 1 V13 M1 7 H13" stroke="#111" stroke-width="2"/></svg></div>
</div>
<a class="btn-gold faq-cta">Check Our FAQ for More Answers</a>

<section class="cta-banner">
  <h2>Start Today with Eco-Friendly Laundry – No Plastic, No Hassle.<br>Just Fresh Laundry</h2>
  <a class="order-btn">Order Now</a>
</section>

<footer class="site-footer">
  <div class="brand"><span class="brand-mark"></span>Plooifris</div>
  <div class="footer-col" style="left:420px"><svg viewBox="0 0 20 20" fill="none" stroke="#fff" stroke-width="1.6"><path d="M10 18 C5 12 4 9 4 7.5 A6 6 0 0 1 16 7.5 C16 9 15 12 10 18Z"/><circle cx="10" cy="7.5" r="2"/></svg><span>12 Linnenstraat,<br>1012 AB Amsterdam</span></div>
  <div class="footer-col" style="left:630px"><svg viewBox="0 0 20 20" fill="none" stroke="#fff" stroke-width="1.6"><path d="M5 3 L8 3 L9 7 L7 8.5 C8 11 9 12 11.5 13 L13 11 L17 12 V15 C17 16 16 17 15 17 C9 16.5 3.5 11 3 5 C3 4 4 3 5 3Z"/></svg><span>Call :<br>020 555 0148</span></div>
  <div class="footer-col" style="left:860px"><svg viewBox="0 0 20 20" fill="none" stroke="#fff" stroke-width="1.6"><rect x="2.5" y="4.5" width="15" height="11" rx="1"/><path d="M3 5 L10 11 L17 5"/></svg><span>Email :<br>info@plooifris.nl</span></div>
  <div class="footer-rule"></div>
  <p class="copyright">All rights reserved © 2024 Plooifris</p>
  <div class="socials"><span></span><span></span><span></span></div>
</footer>

</body>
</html>
```